INNOVATIVE DESIGN NEEDED FOR FINANCIAL COMPANY

INTERNATIONAL FIRM IN HONG KONG NEEDS A MODERN BUSINESS CARD DESIGN. ONE SIDE ENGLISH OTHER SIDE IN CHINESE. WE ARE OPEN TO CHANGING FONTS AND COLOR. SHOULD BE A CARD THAT IS PROFESSIONAL DEALING WITH HIGH NET WORTH CLIENTELE. BOTH SIDES OF THE CARD WILL BE THE SAME, HOWEVER, THE WORDING ON ONE SIDE WILL BE ENGLISH AND THE OTHER SIDE IN CHINESE (CAN ASSIST IN THE LETTERING - CAN PROVIDE ONCE CARD DESIGN IS ACCEPTED.

Target Market(s)

Hong Kong/CHINA

Contact Information for Business Card

ATTRACTIVE MODERN

```html
<!DOCTYPE html>
<html lang="en">
<head>
<meta charset="utf-8">
<title>Linden Asset Management – Business Cards</title>
<link href="https://fonts.googleapis.com/css2?family=Poppins:wght@400;500&family=Roboto:wght@400&family=Noto+Sans+SC:wght@400;700&display=swap" rel="stylesheet">
<style>
  :root {
    --bg: #e6e6e6;
    --card: #ffffff;
    --green: #1a9168;
    --dark: #3d3d3d;
    --ink: #4a4a4a;
    --rule: #d6d6d6;
  }
  html, body { margin: 0; padding: 0; }
  body {
    width: 1200px; height: 1200px; overflow: hidden;
    background: var(--bg);
    position: relative;
    font-family: "Poppins", sans-serif;
  }
  .card {
    position: absolute; left: 257px;
    width: 686px; height: 392px;
    background: var(--card);
    box-shadow: 0 18px 30px rgba(0,0,0,0.25);
    overflow: hidden;
  }
  .card--english { top: 160px; }
  .card--chinese { top: 648px; font-family: "Roboto", sans-serif; }

  .brand { position: absolute; top: 172px; display: flex; align-items: center; gap: 10px; }
  .card--english .brand { left: 77px; }
  .card--chinese .brand { left: 69px; }
  .brand__dot { width: 46px; height: 46px; border-radius: 50%; background: var(--green); flex: none; }
  .brand__name { color: var(--dark); font-family: "Noto Sans SC", sans-serif; font-weight: 700; line-height: 1; }
  .brand__zh { display: block; font-size: 19px; letter-spacing: 1px; }
  .brand__en { display: block; font-size: 10px; letter-spacing: 1.3px; margin-top: 4px; }

  .divider { position: absolute; top: 100px; width: 1px; height: 200px; background: var(--rule); }
  .card--english .divider { left: 383px; }
  .card--chinese .divider { left: 376px; top: 80px; height: 230px; }

  .details { position: absolute; color: var(--ink); }
  .card--english .details { left: 411px; top: 94px; }
  .card--chinese .details { left: 405px; top: 86px; }
  .details__name { margin: 0; color: var(--green); font-weight: 500; font-size: 27px; line-height: 1.1; }
  .card--chinese .details__name { font-family: "Noto Sans SC", sans-serif; font-weight: 400; font-size: 26px; }
  .details__role { margin: 2px 0 0; font-size: 17px; line-height: 1.2; }
  .card--chinese .details__role { font-family: "Noto Sans SC", sans-serif; margin-top: 8px; }
  .details__address { margin: 14px 0 0; font-size: 16px; line-height: 21px; font-style: normal; }
  .card--chinese .details__address { margin-top: 12px; }
  .card--chinese .zh { font-family: "Noto Sans SC", sans-serif; }
  .contacts { list-style: none; margin: 11px 0 0; padding: 0; font-size: 16.5px; }
  .contacts li { display: flex; align-items: center; height: 22px; }
  .contacts svg { width: 16px; height: 16px; fill: var(--green); margin-right: 10px; flex: none; }

  .band { position: absolute; left: 0; bottom: 0; width: 686px; height: 36px; }
  .website {
    position: absolute; bottom: 7px; color: #fff;
    font-family: "Poppins", sans-serif; font-size: 16px; letter-spacing: 4px;
  }
  .card--english .website { right: 20px; }
  .card--chinese .website { left: 24px; }
</style>
</head>
<body>
<svg width="0" height="0" style="position:absolute">
  <defs>
    <symbol id="icon-phone" viewBox="0 0 16 16"><path d="M3.2 1.2l2.3 2.8-1.2 1.6c.9 2 2.2 3.3 4.2 4.2l1.6-1.2 2.8 2.3-1.5 2.3C6.8 13 3 9.2 1 3.6z"/></symbol>
    <symbol id="icon-mobile" viewBox="0 0 16 16"><path d="M4 1h8v14H4zM5.5 2.8v9.4h5V2.8z"/></symbol>
    <symbol id="icon-fax" viewBox="0 0 16 16"><path d="M4.5 1h7v5h-7zM1 7h14v6H1zM3 14h10v1.5H3z"/><rect x="5" y="9" width="6" height="1.3" fill="#fff"/></symbol>
    <symbol id="icon-mail" viewBox="0 0 16 16"><path d="M1 4h14v9H1zM2.5 5.3L8 9.3l5.5-4z" fill-rule="evenodd"/></symbol>
  </defs>
</svg>

<section class="card card--english" lang="en">
  <div class="brand">
    <span class="brand__dot"></span>
    <span class="brand__name"><span class="brand__zh" lang="zh-Hant">林登資產管理有限公司</span><span class="brand__en">Linden Asset Management Ltd</span></span>
  </div>
  <div class="divider"></div>
  <div class="details">
    <h2 class="details__name">Daniel Harper</h2>
    <p class="details__role">President</p>
    <address class="details__address">4120 Willow Bend Road<br>Juneau, Alaska 36218</address>
    <ul class="contacts">
      <li><svg><use href="#icon-phone"/></svg>482-307-1146</li>
      <li><svg><use href="#icon-mobile"/></svg>482-619-2053</li>
      <li><svg><use href="#icon-fax"/></svg>482-774-3390</li>
      <li><svg><use href="#icon-mail"/></svg>hello@lindenam.com</li>
    </ul>
  </div>
  <svg class="band" viewBox="0 0 686 36" preserveAspectRatio="none">
    <rect x="0" y="24" width="686" height="12" fill="#3d3d3d"/>
    <polygon points="398,36 434,0 686,0 686,36" fill="#1a9168"/>
  </svg>
  <span class="website">www.lindenam.com</span>
</section>

<section class="card card--chinese" lang="zh-Hans">
  <div class="brand">
    <span class="brand__dot"></span>
    <span class="brand__name"><span class="brand__zh" lang="zh-Hant">林登資產管理有限公司</span><span class="brand__en" lang="en">Linden Asset Management Ltd</span></span>
  </div>
  <div class="divider"></div>
  <div class="details">
    <h2 class="details__name">丹尼尔哈珀</h2>
    <p class="details__role">主席</p>
    <address class="details__address">4120 Willow Bend Road<br><span class="zh">朱诺, 阿拉斯加州36218</span></address>
    <ul class="contacts">
      <li><svg><use href="#icon-phone"/></svg>482-307-1146</li>
      <li><svg><use href="#icon-mobile"/></svg>482-619-2053</li>
      <li><svg><use href="#icon-fax"/></svg>482-774-3390</li>
      <li><svg><use href="#icon-mail"/></svg>hello@lindenam.com</li>
    </ul>
  </div>
  <svg class="band" viewBox="0 0 686 36" preserveAspectRatio="none">
    <rect x="0" y="24" width="686" height="12" fill="#3d3d3d"/>
    <polygon points="0,0 256,0 292,36 0,36" fill="#1a9168"/>
  </svg>
  <span class="website">www.lindenam.com</span>
</section>
</body>
</html>
```